Business Coaching Model and Flow Chart

We need this flowchart, attached, to be updated in a modern and engaging way. This flowchart is the cornerstone of a business coaching class we are running, and will be the main support reference for the people who take the class. We are open to ideas as to how it is presented, but we would like a largely minimalist look that leaves space to be impactful where the key information sites. Our colour scheme is primary red (D51C29), white, grey (333333), black, and secondary green (3C8740). We will also need our logo present (attached).

```html
<!DOCTYPE html>
<html lang="en">
<head>
<meta charset="utf-8">
<title>Groups to Teams Through Learning Together</title>
<link rel="stylesheet" href="https://fonts.googleapis.com/css2?family=Poppins:wght@400;500;700&display=swap">
<style>
  :root {
    --red: #d51c29;
    --grey: #333333;
    --black: #000000;
    --white: #ffffff;
    --green: #3c8740;
    --filler: #cccccc;
    --divider: rgba(255,255,255,0.35);
  }
  * { box-sizing: border-box; margin: 0; padding: 0; }
  html, body { width: 1200px; height: 848px; overflow: hidden; background: var(--white); }
  body { position: relative; font-family: "Poppins", Arial, sans-serif; }

  .masthead {
    position: absolute; left: 0; top: 0; width: 1200px; height: 158px;
    background: var(--black);
    display: flex; align-items: center; justify-content: center;
  }
  .brand-name {
    font-family: "Poppins", Arial, sans-serif; font-weight: 500;
    font-size: 22px; letter-spacing: 3px; color: var(--white);
  }

  .title {
    position: absolute; top: 175px; left: 0; width: 1200px; text-align: center;
    font-family: "Poppins", Arial, sans-serif; font-weight: 700; font-size: 24px;
    color: var(--black);
  }

  .stage-band { position: absolute; left: 0; top: 229px; width: 1200px; height: 66px; }
  .stage-label {
    position: absolute; top: 229px; height: 54px;
    display: flex; align-items: center; justify-content: center; text-align: center;
    color: var(--white); font-size: 12.5px; line-height: 1.3;
  }
  .stage-label.solution { font-size: 14px; }

  .column {
    position: absolute; top: 296px; height: 537px; width: 161px;
    display: flex; flex-direction: column; gap: 7px;
  }
  .step {
    background: var(--grey); color: var(--white); font-size: 12px; line-height: 1.3;
    padding: 0 4px 0 17px; min-height: 40px; display: flex; align-items: center;
    position: relative; letter-spacing: -0.1px;
  }
  .step.tall { min-height: 41px; }
  .step.opens::after {
    content: ""; position: absolute; left: 20px; bottom: -7px;
    border-left: 7px solid transparent; border-right: 7px solid transparent;
    border-top: 7px solid var(--grey);
  }
  .topic {
    background: var(--red); color: var(--white); font-size: 11.5px; line-height: 1.15;
    min-height: 30px; padding: 0 2px 0 27px; display: flex; align-items: center; position: relative;
    letter-spacing: -0.1px;
  }
  .topic::before {
    content: ""; position: absolute; left: 16px; top: 50%; width: 5px; height: 5px;
    margin-top: -2.5px; border-radius: 50%; background: var(--white);
  }
  .filler { background: var(--filler); flex: 1; }

  .outcome-list {
    position: absolute; top: 296px; height: 537px; width: 161px;
    display: flex; flex-direction: column; padding: 4px 10px;
  }
  .outcome-list.problems { left: 13px; background: var(--red); }
  .outcome-list.solutions { left: 1027px; background: var(--green); }
  .outcome {
    flex: 1; display: flex; flex-direction: column; align-items: center; justify-content: flex-end;
    gap: 4px; padding-bottom: 6px; color: var(--white); font-size: 11.5px; line-height: 1.3;
    text-align: center; border-bottom: 1px solid var(--divider); white-space: nowrap;
  }
  .outcome:last-child { border-bottom: none; }
  .icon-slot { width: 34px; height: 30px; border-radius: 6px; background: rgba(255,255,255,0.85); }
</style>
</head>
<body>

<header class="masthead">
  <div class="brand-name">Mara Kessel</div>
</header>

<h1 class="title">GROUPS TO TEAMS THROUGH LEARNING TOGETHER</h1>

<svg class="stage-band" viewBox="0 229 1200 66" aria-hidden="true">
  <polygon fill="#d51c29" points="13,229 174,229 190,256 174,283 13,283"/>
  <polygon fill="#333333" points="180,229 343,229 359,256 343,283 180,283 196,256"/>
  <polygon fill="#333333" points="349,229 513,229 529,256 513,283 349,283 365,256"/>
  <polygon fill="#333333" points="519,229 682,229 698,256 682,283 519,283 535,256"/>
  <polygon fill="#333333" points="688,229 852,229 868,256 852,283 688,283 704,256"/>
  <polygon fill="#333333" points="858,229 1022,229 1038,256 1022,283 858,283 874,256"/>
  <polygon fill="#3c8740" points="1028,229 1188,229 1188,283 1028,283 1044,256"/>
  <polygon fill="#d51c29" points="86,283 100,283 93,295"/>
  <polygon fill="#333333" points="255,283 269,283 262,295"/>
  <polygon fill="#333333" points="424,283 438,283 431,295"/>
  <polygon fill="#333333" points="593,283 607,283 600,295"/>
  <polygon fill="#333333" points="762,283 776,283 769,295"/>
  <polygon fill="#333333" points="931,283 945,283 938,295"/>
  <polygon fill="#3c8740" points="1100,283 1114,283 1107,295"/>
</svg>

<div class="stage-label" style="left:13px;width:161px;">Problem</div>
<div class="stage-label" style="left:180px;width:163px;">Clarify challenges<br>Diagnostics</div>
<div class="stage-label" style="left:349px;width:164px;">Planning for Success<br>Make a Plan</div>
<div class="stage-label" style="left:519px;width:163px;">Learn the tools<br>Workshops</div>
<div class="stage-label" style="left:688px;width:164px;">Doing Mastering<br>the Tools</div>
<div class="stage-label" style="left:858px;width:164px;">Reflect-Adapt<br>Embed</div>
<div class="stage-label solution" style="left:1028px;width:160px;">Solution</div>

<section class="outcome-list problems">
  <div class="outcome"><div class="icon-slot" role="img" aria-label="Invoice icon"></div>Underbilling</div>
  <div class="outcome"><div class="icon-slot" role="img" aria-label="Group of staff icon"></div>Staff Retention</div>
  <div class="outcome"><div class="icon-slot" role="img" aria-label="Search for person icon"></div>Hard to recruit</div>
  <div class="outcome"><div class="icon-slot" role="img" aria-label="Alert message icon"></div>Client Complaints</div>
  <div class="outcome"><div class="icon-slot" role="img" aria-label="Stressed expression icon"></div>Staff Stress and Burnout</div>
  <div class="outcome"><div class="icon-slot" role="img" aria-label="Clashing arrows icon"></div>Conflict</div>
  <div class="outcome"><div class="icon-slot" role="img" aria-label="Reversing arrows icon"></div>CSF Constant Change</div>
  <div class="outcome"><div class="icon-slot" role="img" aria-label="Hourglass icon"></div>Limited in Best Practice</div>
</section>

<section class="column" style="left:182px;">
  <div class="step">Scoping</div>
  <div class="step tall">Interviews</div>
  <div class="step">Group reflection</div>
  <div class="step">Opinion Surveys</div>
  <div class="step tall">Certified</div>
  <div class="step opens">Assessments</div>
  <div class="topic">Personality</div>
  <div class="topic">Styles</div>
  <div class="topic">Work</div>
  <div class="topic">Preference</div>
  <div class="topic">Strengths &amp; Values</div>
  <div class="topic">Trust</div>
  <div class="topic">360</div>
</section>

<section class="column" style="left:351px;">
  <div class="step tall">Team data analysis<br>Workshop</div>
  <div class="step tall">Individual<br>Development Plan</div>
  <div class="step tall">Team Development<br>Plan</div>
  <div class="step tall">Organisational Plan</div>
  <div class="filler"></div>
</section>

<section class="column" style="left:520px;">
  <div class="step tall" style="white-space:nowrap;">Foundation Workshops</div>
  <div class="topic" style="white-space:nowrap;">Difficult Conversations</div>
  <div class="topic">Giving &amp; Receiving<br>Feedback</div>
  <div class="topic">Values Alignment</div>
  <div class="topic">Shared Purpose</div>
  <div class="topic">Ways of Working</div>
  <div class="topic">Diversity</div>
  <div class="topic">Wellbeing</div>
  <div class="topic">Time Management</div>
  <div class="step tall" style="white-space:nowrap;">Customised Workshops</div>
  <div class="filler"></div>
</section>

<section class="column" style="left:689px;">
  <div class="step tall">Group Coaching</div>
  <div class="step tall">Team Coaching</div>
  <div class="step tall">Individual Coaching</div>
  <div class="step tall">Peer Learning</div>
  <div class="step tall">Lunch ’n Learn</div>
  <div class="filler"></div>
</section>

<section class="column" style="left:858px;">
  <div class="step">Culture Committee</div>
  <div class="step" style="white-space:nowrap;">Embedding Workshop</div>
  <div class="step">Culture Collateral</div>
  <div class="step">Wow Manifesto</div>
  <div class="step">Leadership Team<br>Coaching</div>
  <div class="step">Measure ROI</div>
  <div class="step">Review Success</div>
  <div class="step">Evaluation Surveys</div>
  <div class="step">Temperature Checks</div>
  <div class="step">Recruit to Suit</div>
  <div class="step">Future Proofing<br>What next?</div>
  <div class="filler"></div>
</section>

<section class="outcome-list solutions">
  <div class="outcome"><div class="icon-slot" role="img" aria-label="Person icon"></div>Self awareness &amp;<br>Ownership</div>
  <div class="outcome"><div class="icon-slot" role="img" aria-label="Handshake icon"></div>Partnership</div>
  <div class="outcome"><div class="icon-slot" role="img" aria-label="Workplace desk icon"></div>Great Place to Work</div>
  <div class="outcome"><div class="icon-slot" role="img" aria-label="Growing mind icon"></div>Growth Mindset</div>
  <div class="outcome"><div class="icon-slot" role="img" aria-label="Megaphone icon"></div>Coach Approach<br>Culture</div>
  <div class="outcome"><div class="icon-slot" role="img" aria-label="Star rating icon"></div>Feedback Culture</div>
  <div class="outcome"><div class="icon-slot" role="img" aria-label="Gear icon"></div>Way to manage conflict</div>
  <div class="outcome"><div class="icon-slot" role="img" aria-label="Speech bubbles icon"></div>Best practice<br>Communication Skills</div>
</section>

</body>
</html>
```